Postcard Mail Out - Wendell

We are a real estate company. We need a post card to mail out to potential clients to try and sale their land. We will attached a couple of post cards that we like but we do not want to copy them completely. We do need to put the Fair Dwelling Access and the Homebroker logos with a disclosure saying not intended to solicit currently listed properties. The image below is what we had started working on. We would like to include something about farm land, timber, maybe a pond, something along those lines. The PDF Files attached are a flyer that was mailed out by another company that we do not want to copy completely. Attached also will be our company's Logo.

Requirements
Must have
• We do need to put the Fair Dwelling Access and the Homebroker logos with a disclosure saying not intended to solicit currently listed properties.<br/><br/>At Cal Moreno Summit Realty, we are blessed to have one of the very best Rural Land Specialists available. Wendell has years of experience promoting and selling rural land properties. Wendell has earned the trust of many landowners, as he is so PASSIONATE in all regards to rural land, farms and ranches. He has made a wide range of landowners very happy throughout his years in Real Estate. Call him today and show him your property, and he will provide you with a free analysis and strategy to maximize the return on your property.
Nice to have
• A picture of Wendell has been added to use on the back of the post card with his phone and number. It would be nice to have a east Texas scenery picture behind him instead of an office.<br/><br/>Please include front and back of post card in your submission.
Should not have
• Should not have Ferris Dunmore's information on the postcard. That post card was just to show what we was wanting. The agent we want listed is Wendell Pruitt and his phone number is (555)413-2086.

```html
<!DOCTYPE html>
<html lang="en">
<head>
<meta charset="utf-8">
<title>Land For Sale? Postcard – Front and Back</title>
<link href="https://fonts.googleapis.com/css2?family=Cinzel:wght@600;700&family=Open+Sans:wght@400;600;700;800&display=swap" rel="stylesheet">
<style>
  :root {
    --backdrop: #d5d5d5;
    --card-white: #f7f7f7;
    --brand-blue: #1b6aa8;
    --deep-blue: #0e4f86;
    --ink: #1f2a36;
    --line-blue: #2c3fa0;
    --sky: #3f86d9;
    --title-outline: #0d4a96;
    --white: #ffffff;
  }
  * { box-sizing: border-box; margin: 0; padding: 0; }
  html, body { width: 1200px; height: 696px; overflow: hidden; }
  body {
    background: var(--backdrop);
    font-family: "Open Sans", Arial, sans-serif;
    position: relative;
  }
  .postcard {
    position: absolute;
    top: 153px;
    width: 570px;
    height: 390px;
    overflow: hidden;
    box-shadow: 0 6px 14px rgba(0,0,0,.25);
  }

  /* ---------- Back side ---------- */
  .postcard--back { left: 20px; background: var(--card-white); }
  .back-scenery {
    position: absolute; inset: 0;
    background: linear-gradient(160deg, #f4f4f4 0%, #dcdcdc 45%, #c9c9c9 70%, #e6e6e6 100%);
    opacity: .75;
  }
  .back-scenery::after {
    content: ""; position: absolute; inset: 0;
    background: linear-gradient(90deg, rgba(255,255,255,.85) 0%, rgba(255,255,255,.4) 55%, rgba(255,255,255,.2) 100%);
  }
  .brand {
    position: absolute; left: 34px; top: 34px;
    display: flex; align-items: center; gap: 10px;
  }
  .brand-dot { width: 26px; height: 26px; border-radius: 50%; background: var(--deep-blue); }
  .brand-name {
    font-family: "Cinzel", Georgia, serif; font-weight: 700;
    font-size: 20px; color: var(--deep-blue); line-height: 1.1;
  }
  .tagline {
    position: absolute; left: 40px; top: 100px;
    font-family: "Cinzel", Georgia, serif; font-weight: 700;
    font-size: 22px; line-height: 1.15; color: var(--deep-blue);
  }
  .fair-access {
    position: absolute; left: 40px; top: 180px;
    font-family: "Cinzel", Georgia, serif; font-weight: 600;
    font-size: 21px; line-height: 1.15; color: var(--brand-blue);
  }
  .agent-name {
    position: absolute; left: 44px; top: 252px;
    font-weight: 700; font-size: 22px; color: var(--ink);
  }
  .agent-phone {
    position: absolute; left: 40px; top: 280px;
    font-weight: 700; font-size: 32px; color: var(--brand-blue); letter-spacing: .5px;
  }
  .contact-band {
    position: absolute; left: 0; bottom: 0; width: 100%; height: 50px;
  }
  .contact-text {
    position: absolute; left: 16px; bottom: 10px;
    color: var(--white); font-size: 8.5px; line-height: 1.5; font-weight: 600;
  }
  .contact-text svg { width: 9px; height: 9px; vertical-align: -1px; fill: var(--white); margin-right: 3px; }
  .broker-mark {
    position: absolute; right: 16px; top: 8px;
    display: flex; align-items: center; gap: 6px;
    color: var(--white); font-size: 11px; font-weight: 700;
  }
  .broker-square { width: 12px; height: 12px; background: var(--white); }
  .disclosure {
    position: absolute; right: 16px; bottom: 8px;
    color: var(--white); font-size: 7.5px; font-weight: 400;
  }
  .divider-stripe { position: absolute; inset: 0; width: 100%; height: 100%; }
  .photo-bubble {
    position: absolute; width: 64px; height: 64px; border-radius: 50%;
    border: 4px solid var(--white); box-shadow: 0 2px 5px rgba(0,0,0,.35);
  }
  .bubble-1 { left: 356px; top: 42px;  background: linear-gradient(#6fb0ea 0%, #9fd0f2 45%, #5f9a3a 60%, #3f7a28 100%); }
  .bubble-2 { left: 326px; top: 112px; background: linear-gradient(#3d8ee0 0%, #8cc6f0 50%, #6f9c48 62%, #a3a08a 100%); }
  .bubble-3 { left: 296px; top: 182px; background: linear-gradient(#2f7fd6 0%, #8dbbe6 45%, #4f8a2f 60%, #2f5e22 100%); }
  .bubble-4 { left: 266px; top: 252px; background: linear-gradient(#3e6fb3 0%, #9bb6d9 45%, #3c85c4 70%, #244f7d 100%); }
  .stamp-box {
    position: absolute; right: 40px; top: 62px;
    width: 94px; height: 68px; border: 1px solid var(--line-blue);
  }
  .address-line {
    position: absolute; right: 42px; height: 1px; background: var(--line-blue);
  }
  .line-1 { top: 170px; left: 398px; }
  .line-2 { top: 208px; left: 370px; }
  .line-3 { top: 246px; left: 370px; }
  .line-4 { top: 284px; left: 340px; }

  /* ---------- Front side ---------- */
  .postcard--front { left: 610px; background: var(--white); display: flex; gap: 4px; }
  .scene-strip { flex: 1; height: 100%; position: relative; }
  .strip-rail    { background: linear-gradient(#bcd8ef 0%, #9bb98a 22%, #7f8f5f 50%, #b99f75 80%, #8f8a6a 100%); }
  .strip-silos   { background: linear-gradient(var(--sky) 0%, #7fb3e8 30%, #c9ced3 50%, #a99373 70%, #b9a589 100%); }
  .strip-valley  { background: linear-gradient(#4f86c9 0%, #7f8f70 20%, #9a7a2a 38%, #3f6a2a 65%, #2f5a26 100%); }
  .strip-pasture { background: linear-gradient(#a9dcef 0%, #c8c1a8 30%, #a89a7c 50%, #bfb6a2 75%, #aca08a 100%); }
  .strip-orchard { background: linear-gradient(#8fb6e6 0%, #a59676 25%, #7d6a3a 50%, #8a7340 75%, #6f5a2e 100%); }
  .title-band {
    position: absolute; left: 0; right: 0; top: 62px; height: 96px;
    background: rgba(255,255,255,.5);
    display: flex; align-items: center; justify-content: center;
  }
  .front-title {
    font-weight: 800; font-size: 52px; color: var(--white); letter-spacing: .5px;
    -webkit-text-stroke: 2px var(--title-outline);
    paint-order: stroke fill;
    transform: rotate(-10deg);
    text-shadow: 0 2px 3px rgba(0,0,0,.3);
  }
</style>
</head>
<body>

  <section class="postcard postcard--back" aria-label="Postcard back">
    <div class="back-scenery" role="img" aria-label="Faded photo of a stone country house"></div>

    <svg class="divider-stripe" viewBox="0 0 570 390" preserveAspectRatio="none" aria-hidden="true">
      <polygon points="380,0 392,0 290,390 278,390" fill="var(--brand-blue)"/>
      <polygon points="0,340 570,340 570,390 0,390" fill="var(--brand-blue)"/>
      <polygon points="0,340 300,340 287,390 0,390" fill="var(--deep-blue)"/>
    </svg>

    <div class="brand">
      <span class="brand-dot"></span>
      <span class="brand-name">Cal Moreno<br>Summit Realty</span>
    </div>

    <p class="tagline">Specializing in<br>Rural Land Sales</p>
    <p class="fair-access">Fair Dwelling<br>Access</p>
    <p class="agent-name">Wendell Pruitt</p>
    <p class="agent-phone">(555)413-2086</p>

    <div class="photo-bubble bubble-1" role="img" aria-label="Red barn in a green field"></div>
    <div class="photo-bubble bubble-2" role="img" aria-label="Country road lined with trees"></div>
    <div class="photo-bubble bubble-3" role="img" aria-label="Farmhouse beside crop rows"></div>
    <div class="photo-bubble bubble-4" role="img" aria-label="Large home with a fountain"></div>

    <div class="stamp-box"></div>
    <div class="address-line line-1"></div>
    <div class="address-line line-2"></div>
    <div class="address-line line-3"></div>
    <div class="address-line line-4"></div>

    <div class="contact-band">
      <p class="contact-text">
        <svg viewBox="0 0 10 10"><path d="M2 0.5 L3.8 2.6 L3 3.8 Q4 6 6.2 7 L7.4 6.2 L9.5 8 L8.4 9.5 Q3 9 0.5 1.6 Z"/></svg>(555)413-2086 &nbsp;www.summitlandtx.com<br>
        <svg viewBox="0 0 10 10"><path d="M5 0 A3.5 3.5 0 0 1 8.5 3.5 Q8.5 6 5 10 Q1.5 6 1.5 3.5 A3.5 3.5 0 0 1 5 0 Z M5 2.2 A1.3 1.3 0 1 0 5 4.8 A1.3 1.3 0 1 0 5 2.2 Z"/></svg>418 W Oak St. Pinecrest, TX 75501. Directions.
      </p>
      <div class="broker-mark"><span class="broker-square"></span>Homebroker</div>
      <p class="disclosure">Not intended to solicit currently listed properties.</p>
    </div>
  </section>

  <section class="postcard postcard--front" aria-label="Postcard front">
    <div class="scene-strip strip-rail" role="img" aria-label="Aerial view of a train on tracks through open land"></div>
    <div class="scene-strip strip-silos" role="img" aria-label="Grain silos on a dirt farm lot"></div>
    <div class="scene-strip strip-valley" role="img" aria-label="Green valley with autumn trees and a farmhouse"></div>
    <div class="scene-strip strip-pasture" role="img" aria-label="Dry pasture with grazing cattle below rocks"></div>
    <div class="scene-strip strip-orchard" role="img" aria-label="Hillside orchard rows"></div>
    <div class="title-band">
      <h1 class="front-title">Land For Sale?</h1>
    </div>
  </section>

</body>
</html>
```